UX/UI Design of mobile application for language learning through picture cards

We are looking for a Mobile Application Designer with knowledge of UX/UI concepts.

We best candidate is a skilled Mobile Application Designer with knowledge of last trends and with experience in completing similar tasks.

This is a test task. After successful completion, the best candidate will be given a full task.

```html
<!DOCTYPE html>
<html lang="en">
<head>
<meta charset="utf-8">
<title>Picture Cards – Quiz</title>
<link rel="stylesheet" href="https://fonts.googleapis.com/css2?family=Roboto:wght@400;500&display=swap">
<style>
  :root {
    --brand-blue: #0a7bff;
    --accent-orange: #ff9500;
    --accent-green: #1fd36a;
    --accent-red: #ff3358;
    --highlight-yellow: #ffc400;
    --panel-dark: #2a2a2a;
    --pill-dark: #3b3b3b;
    --photo-dark: #1b2419;
    --white: #ffffff;
  }
  * { box-sizing: border-box; margin: 0; padding: 0; }
  html, body { width: 675px; height: 1200px; overflow: hidden; }
  body {
    position: relative;
    font-family: "Roboto", Arial, sans-serif;
    color: var(--white);
    background: var(--panel-dark);
  }
  .app-header {
    position: absolute; left: 0; top: 0; width: 675px; height: 115px;
    background: var(--brand-blue);
  }
  .status-bar {
    position: absolute; left: 0; top: 0; width: 100%; height: 36px;
    font-size: 21px; display: flex; align-items: center;
  }
  .status-carrier { position: absolute; left: 10px; display: flex; align-items: center; gap: 4px; }
  .status-time { position: absolute; left: 0; width: 100%; text-align: center; font-weight: 500; }
  .status-battery { position: absolute; right: 12px; display: flex; align-items: center; gap: 8px; }
  .menu-button { position: absolute; left: 22px; top: 58px; }
  .language-picker {
    position: absolute; left: 0; width: 100%; top: 62px; text-align: center;
    font-size: 25px; font-weight: 500;
  }
  .language-picker svg { vertical-align: middle; margin-left: 10px; }
  .photo-stage {
    position: absolute; left: 0; top: 115px; width: 675px; height: 637px;
    background: radial-gradient(ellipse at 40% 60%, #3a4432 0%, #222b1f 55%, var(--photo-dark) 100%);
  }
  .photo-focus {
    position: absolute; left: 59px; top: 194px; width: 566px; height: 486px;
    background: linear-gradient(135deg, #6a6f63 0%, #8c8d84 35%, #5d5f57 65%, #3d3f38 100%);
    border: 1px solid rgba(255,255,255,0.5);
  }
  .focus-bracket { position: absolute; left: 47px; top: 185px; }
  .action-panel {
    position: absolute; left: 0; top: 752px; width: 675px; height: 448px;
    background: var(--panel-dark);
  }
  .action-icon { position: absolute; top: 27px; width: 72px; height: 72px; border-radius: 50%;
    display: flex; align-items: center; justify-content: center; }
  .icon-cards { left: 36px; background: var(--brand-blue); }
  .icon-sound { left: 162px; background: var(--accent-orange); }
  .icon-share { left: 288px; background: var(--accent-green); }
  .icon-close { position: absolute; left: 588px; top: 41px; width: 44px; height: 44px; border-radius: 50%;
    background: var(--accent-red); display: flex; align-items: center; justify-content: center; }
  .quiz-question {
    position: absolute; left: 0; top: 152px; width: 100%; text-align: center;
    font-size: 36px; line-height: 43px; font-weight: 400;
  }
  .answer-pill {
    position: absolute; top: 341px; height: 72px; border-radius: 36px;
    display: flex; align-items: center; justify-content: center; font-size: 25px;
    white-space: nowrap;
  }
  .answer-pill.is-selected { left: 36px; width: 288px; background: var(--brand-blue); }
  .answer-pill.option-b { left: 342px; width: 207px; background: var(--pill-dark); }
  .answer-pill.option-c { left: 567px; width: 207px; background: var(--pill-dark); }
</style>
</head>
<body>
  <header class="app-header">
    <div class="status-bar">
      <span class="status-carrier">
        <svg width="48" height="10" viewBox="0 0 48 10"><g fill="#fff"><circle cx="5" cy="5" r="4"/><circle cx="15" cy="5" r="4"/><circle cx="25" cy="5" r="4"/></g><g fill="none" stroke="#fff" stroke-width="1.4"><circle cx="35" cy="5" r="3.5"/><circle cx="44" cy="5" r="3.5"/></g></svg>
        NOVA
        <svg width="20" height="16" viewBox="0 0 20 16"><path d="M10 15 L1 5 A13 13 0 0 1 19 5 Z" fill="#fff"/></svg>
      </span>
      <span class="status-time">9:41 AM</span>
      <span class="status-battery">
        <svg width="12" height="20" viewBox="0 0 12 20"><path d="M1 6 L11 14 L6 18 L6 2 L11 6 L1 14" fill="none" stroke="#fff" stroke-width="1.6"/></svg>
        58 %
        <svg width="44" height="20" viewBox="0 0 44 20"><rect x="1" y="2" width="38" height="16" rx="3" fill="none" stroke="#fff" stroke-width="1.6"/><rect x="4" y="5" width="20" height="10" fill="#fff"/><rect x="40" y="7" width="3" height="6" fill="#fff"/></svg>
      </span>
    </div>
    <svg class="menu-button" width="41" height="36" viewBox="0 0 41 36"><g fill="#fff"><rect y="0" width="41" height="6" rx="3"/><rect y="15" width="41" height="6" rx="3"/><rect y="30" width="41" height="6" rx="3"/></g></svg>
    <div class="language-picker">English<svg width="18" height="10" viewBox="0 0 18 10"><path d="M0 0 H18 L9 10 Z" fill="#fff"/></svg></div>
  </header>

  <section class="photo-stage" role="img" aria-label="Blurred jungle background behind the photo card"></section>
  <div class="photo-focus" role="img" aria-label="Close-up photo of an elephant's head with raised trunk and tusk"></div>
  <svg class="focus-bracket" width="584" height="502" viewBox="0 0 584 502">
    <g fill="none" stroke="var(--highlight-yellow)" stroke-width="7">
      <path d="M3.5 70 V3.5 H70"/>
      <path d="M514 3.5 H580.5 V70"/>
      <path d="M3.5 432 V498.5 H70"/>
      <path d="M514 498.5 H580.5 V432"/>
    </g>
  </svg>

  <main class="action-panel">
    <div class="action-icon icon-cards">
      <svg width="36" height="34" viewBox="0 0 36 34"><rect x="2" y="2" width="26" height="24" rx="3" fill="none" stroke="#fff" stroke-width="3"/><rect x="9" y="9" width="25" height="23" rx="3" fill="#fff"/></svg>
    </div>
    <div class="action-icon icon-sound">
      <svg width="34" height="32" viewBox="0 0 34 32"><path d="M3 11 H10 L20 3 V29 L10 21 H3 Z" fill="#fff"/><path d="M24 9 A9 9 0 0 1 24 23" fill="none" stroke="#fff" stroke-width="3" stroke-linecap="round"/></svg>
    </div>
    <div class="action-icon icon-share">
      <svg width="36" height="34" viewBox="0 0 36 34"><path d="M14 6 H5 A2 2 0 0 0 3 8 V29 A2 2 0 0 0 5 31 H26 A2 2 0 0 0 28 29 V22" fill="none" stroke="#fff" stroke-width="3"/><path d="M11 22 C12 13 18 10 25 10 V4 L34 12 L25 20 V15 C19 15 14 17 11 22 Z" fill="#fff"/></svg>
    </div>
    <div class="icon-close">
      <svg width="18" height="18" viewBox="0 0 18 18"><path d="M3 3 L15 15 M15 3 L3 15" stroke="#fff" stroke-width="3" stroke-linecap="round"/></svg>
    </div>

    <p class="quiz-question">What is highlighted in the<br>picture?</p>

    <div class="answer-pill is-selected">A Elephant</div>
    <div class="answer-pill option-b">Anta</div>
    <div class="answer-pill option-c">Snake</div>
  </main>
</body>
</html>
```